Locksmith SmartPhone Web Design Project

I am a locksmith and focus on customers that use their smart phones to find me. I have a static web page that I created myself but it is horrible. See for yourself at www.brevalkeyworks.com.au

I want a cross-platform static site that simply shows the information and with the ability to change minor items like pricing. I want it to be compelling in its look and feel (not overwhelming) but simple. It must have a; click to call button; the ability to install a hit counter from pagetallyo.com; payment information just like the current graphic of card/cash/quidlo (orla/brixalonte only).

This will be hosted on my own server.
Updates

Hello Designers,

I have updated the brief in the must have and nice to have fields.

Thank you all,

Tom.

Hello to all Designers,

There is about 9 days left before the deadline. The overall level of competition is extremely high and I would like to thank all the designers who have submitted so far, 27 submissions in total so far. Excellent work.

If you have submitted already and wish to provide new designs, I am keen to see them. 

Hi guys, time is almost up. Please submit any new designs that you may have. The quality has been excellent so far.

Tom.

Target Market(s)

People who are locked out of their house/shop/office etc.

Industry/Entity Type

Locksmith

Requirements
Must have
• click to call button
hit counter from pagetallyo
payment graphic card/cash/quidlo (orla/brixalonte only)
cross platform compatibility smartphone/phablet
Single column page preferable, can have two columns.
Nice to have
• When the page loads regardless of the mobile device, all info should be presented. In other words no vertical or horizontal scroll bars.
Should not have
• hidden code, advertising, credits etc

```html
<!DOCTYPE html>
<html lang="en">
<head>
<meta charset="utf-8">
<title>Breval Keyworks</title>
<link rel="stylesheet" href="https://fonts.googleapis.com/css2?family=Oswald:wght@600;700&family=Arimo:wght@400;700&display=swap">
<style>
  :root{
    --bg-top:#13569c;
    --bg-mid:#0e4a8c;
    --bg-bottom:#0b3f7c;
    --band:#0a3a72;
    --white:#ffffff;
    --gold:#f0a830;
    --green:#2f9a10;
    --red:#c8262c;
    --ink:#1a4d8f;
    --line-dark:#0a3566;
    --line-light:#2a66a8;
    --photo-a:#b9a58a;
    --photo-b:#dfe2ec;
    --hero-bg:#eef0f7;
  }
  *{margin:0;padding:0;box-sizing:border-box}
  html,body{width:800px;height:1200px;overflow:hidden}
  body{
    position:relative;
    font-family:"Arimo",Arial,sans-serif;
    color:var(--white);
    background:linear-gradient(180deg,var(--bg-top) 0%,var(--bg-mid) 50%,var(--bg-bottom) 100%);
  }
  .backdrop{position:absolute;inset:0;width:800px;height:1200px}
  .hero{
    position:absolute;left:13px;top:35px;width:774px;height:370px;
    border:5px solid #e8ebf2;border-radius:6px;overflow:hidden;
    background:linear-gradient(90deg,#fdfdfe 0%,var(--hero-bg) 60%,#d9dceb 100%);
  }
  .hero-photo{
    position:absolute;left:0;top:0;width:300px;height:100%;
    background:linear-gradient(90deg,#e9ebf0 0%,var(--photo-a) 45%,var(--photo-b) 100%);
  }
  .hero-name{
    position:absolute;left:300px;right:0;top:95px;
    text-align:center;font-family:"Arimo",Arial,sans-serif;font-weight:700;
    color:var(--red);font-size:60px;line-height:76px;
  }
  .offer{position:absolute;left:0;width:800px;text-align:center}
  .offer-title{top:422px;font-family:"Oswald",sans-serif;font-weight:700;font-size:44px}
  .offer-title .price{font-family:"Arimo",sans-serif;font-weight:400;font-size:46px;margin-left:8px}
  .offer-sub{top:484px;font-family:"Oswald",sans-serif;font-weight:700;font-size:36px;color:var(--gold)}
  .call{
    position:absolute;left:0;width:800px;top:603px;text-align:center;
    font-size:40px;display:flex;justify-content:center;align-items:center;gap:10px;
  }
  .call-number{
    font-weight:700;font-size:48px;color:var(--green);
    -webkit-text-stroke:2px var(--white);paint-order:stroke fill;
  }
  .divider{position:absolute;left:15px;width:770px;height:2px;
    border-top:1px solid var(--line-dark);border-bottom:1px solid var(--line-light)}
  .details{position:absolute;left:0;width:800px;text-align:center;font-weight:700;font-size:33px}
  .details li{list-style:none;position:absolute;left:0;width:800px}
  .payments{position:absolute;top:1004px;left:0;width:800px;display:flex;justify-content:center;gap:58px}
  .pay{
    width:68px;height:45px;border-radius:4px;background:linear-gradient(180deg,#ffffff,#e3e6ea);
    color:var(--ink);font-weight:700;font-size:15px;display:flex;align-items:center;justify-content:center;
    box-shadow:0 2px 3px rgba(0,0,0,.4);
  }
  .status{
    position:absolute;left:0;width:800px;top:1124px;font-size:40px;
    display:flex;justify-content:center;align-items:center;gap:12px;
  }
  .status-dot{width:22px;height:22px;border-radius:50%;background:#f6c637}
  .status-yes{color:var(--gold);font-weight:700;margin-left:14px}
</style>
</head>
<body>
  <svg class="backdrop" viewBox="0 0 800 1200" aria-hidden="true">
    <path d="M0 405 L800 405 L800 445 C720 445 710 555 610 555 L190 555 C90 555 80 445 0 445 Z" fill="#0b3e78" opacity=".7"/>
    <path d="M0 1200 L0 1160 C40 1160 60 1087 140 1087 L660 1087 C740 1087 760 1160 800 1160 L800 1200 Z" fill="var(--band)"/>
  </svg>

  <header class="hero">
    <div class="hero-photo" role="img" aria-label="Photo of a man locked out, leaning his head against a closed door"></div>
    <h1 class="hero-name">BREVAL<br>KEYWORKS</h1>
  </header>

  <p class="offer offer-title">Locked Out?<span class="price">$150</span></p>
  <p class="offer offer-sub">Gets You In. EASY!</p>

  <a class="call">
    <svg width="30" height="30" viewBox="0 0 24 24" aria-hidden="true"><path fill="#fff" d="M6.6 10.8a15 15 0 0 0 6.6 6.6l2.2-2.2c.3-.3.7-.4 1-.2 1.1.4 2.3.6 3.6.6.6 0 1 .4 1 1V20c0 .6-.4 1-1 1A17 17 0 0 1 3 4c0-.6.4-1 1-1h3.5c.6 0 1 .4 1 1 0 1.2.2 2.4.6 3.6.1.3 0 .7-.2 1z"/></svg>
    <span>Click to Call -</span>
    <span class="call-number">0412837560</span>
  </a>

  <div class="divider" style="top:702px"></div>

  <ul class="details">
    <li style="top:742px">ABN: 51207384619</li>
    <li style="top:815px">Master Licence: 302846175</li>
    <li style="top:888px">Hit Number - 1,961</li>
  </ul>

  <div class="divider" style="top:968px"></div>

  <div class="payments">
    <span class="pay">Solvaro</span>
    <span class="pay">orla</span>
    <span class="pay">card</span>
    <span class="pay">quidlo</span>
  </div>

  <p class="status"><span class="status-dot"></span>Locksmith Available?<span class="status-yes">YES</span></p>
</body>
</html>
```